Human Resource Consulting Powerpoint / Word Templates

We need Powerpoint and Word templates to use the same style as our new website. We use Powerpoint and Word when presenting to our clients. These must look professional.
- Proposal template for Powerpoint (8 Page layouts see attached)
- Presentation template for Powerpoint (8 Page layouts see attached)
- Letter head ( 1 page)
- Proposal Template for Word
- Report Template for Word
Theses should include a mini style guide including font size, text positioning on the page and image positioning.
Link to website under construction: http://www.brightmeadow.com.au.42.vornatek.pw/
Our new biz card designs and logo file attached.
Consulting
- Helvetica Nue

```html
<!DOCTYPE html>
<html lang="en">
<head>
<meta charset="utf-8">
<title>BrightMeadow HR – Proposal Template Pages</title>
<link href="https://fonts.googleapis.com/css2?family=Roboto:wght@300;400;500;700&display=swap" rel="stylesheet">
<style>
:root{
  --blue:#1e9be8;
  --bright:#38a4f2;
  --teal:#3fbbd8;
  --slate:#5b84b0;
  --slate-dark:#3f5f80;
  --navy:#1a2230;
  --ink:#222;
  --grey:#555;
  --rule:#cfd5dc;
  --banner-a:#2b3440;
  --banner-b:#56616e;
}
*{box-sizing:border-box;margin:0;padding:0}
html,body{width:948px;height:1200px;overflow:hidden;background:#fff;font-family:"Roboto",Arial,sans-serif;color:var(--ink)}
.sheet{display:grid;grid-template-columns:repeat(3,303px);grid-template-rows:repeat(3,396px);column-gap:13px;row-gap:4px;padding:1px 6px}
.page{position:relative;background:#fff;box-shadow:0 0 3px rgba(0,0,0,.18);overflow:hidden}
.brand-mark{position:absolute;top:13px;right:14px;display:flex;align-items:center;gap:3px;font-size:6.5px;font-weight:500;letter-spacing:.3px;color:var(--navy)}
.brand-mark i{width:9px;height:9px;border-radius:50%;background:var(--blue);display:block}
.banner{position:absolute;left:0;right:0;top:34px;height:64px;background:linear-gradient(100deg,var(--banner-a) 0%,var(--banner-b) 45%,#3a4452 70%,var(--banner-b) 100%)}
.banner-title{position:absolute;left:32px;top:42px;color:#fff;font-weight:300;font-size:30px;letter-spacing:-.5px;line-height:1}
.banner-sub{position:absolute;left:33px;top:76px;color:#e6ebf0;font-weight:300;font-size:11px}
.pager{position:absolute;left:21px;display:flex;flex-direction:column;gap:2.5px}
.pager span{width:5px;height:5px;border-radius:50%;background:var(--blue)}
.pager span.on{background:#444}
.page-no{position:absolute;right:9px;bottom:8px;width:9px;height:9px;border-radius:50%;background:var(--blue)}
.copy{position:absolute;left:43px;right:24px;font-size:6.3px;line-height:8.3px;color:var(--grey);text-align:justify}
.copy p{margin-bottom:2.5px}
.intro{position:absolute;left:42px;width:240px;font-size:6.6px;line-height:9.6px;color:var(--grey)}

/* cover */
.cover-photo{position:absolute;left:0;right:0;top:34px;height:186px;background:linear-gradient(160deg,#3b4654 0%,#69747f 40%,#2f3844 75%,#4a5562 100%)}
.cover-client{position:absolute;top:12px;left:20px;font-size:7px;font-weight:500;color:var(--blue)}
.cover-title{position:absolute;left:37px;top:240px;font-size:38px;font-weight:300;letter-spacing:-.5px;line-height:1}
.cover-org{position:absolute;left:38px;top:280px;font-size:14px;font-weight:300;color:var(--blue)}
.cover-date{position:absolute;left:38px;top:296px;font-size:8.5px;color:var(--grey)}
.cover-bar{position:absolute;left:0;right:0;bottom:0;height:32px;background:var(--navy);color:#fff;display:flex;align-items:center;justify-content:space-between;padding:0 7px}
.party{display:flex;align-items:center;gap:5px;font-size:6px}
.party i{width:10px;height:10px;border-radius:50%;background:var(--blue);display:block}
.party b{display:block;font-weight:400;font-size:8.5px}
.party em{display:block;font-style:normal;color:var(--blue);font-size:5.5px}

/* contents */
.toc-head{position:absolute;left:50px;top:113px;font-size:13px;font-weight:400;letter-spacing:-.2px}
.toc{position:absolute;left:52px;top:140px;list-style:none}
.toc li{display:flex;align-items:center;gap:10px;height:19.7px;font-size:6.5px;color:var(--grey)}
.toc li i{width:10px;height:10px;border-radius:50%;background:var(--blue);border:2px solid #bfe0f7;display:block}

/* table */
.grid-table{position:absolute;left:31px;top:182px;width:242px;height:184px;display:grid;grid-template-columns:95px 72px 75px;border:1px solid var(--rule)}
.col{border-right:1px solid var(--rule);display:flex;flex-direction:column}
.col:last-child{border-right:0}
.col-head{height:44px;color:#fff;font-size:5.5px;font-weight:700;display:flex;flex-direction:column;align-items:center;padding-top:16px;gap:4px}
.col-desc .col-head{background:var(--blue);align-items:flex-start;padding-left:5px;padding-top:20px}
.col-one .col-head{background:var(--slate);padding-top:16px}
.col-two .col-head{background:#3c3f44;padding-top:16px}
.col-head i{width:18px;height:18px;border-radius:50%;background:#fff;display:flex;align-items:center;justify-content:center}
.col-rows{margin-top:22px;padding:0 6px}
.col-rows div{height:15.2px;border-bottom:1px solid var(--rule);font-size:5px;color:var(--grey);display:flex;align-items:center}
.col-one .col-rows div,.col-two .col-rows div{justify-content:center}

/* chart */
.legend{position:absolute;left:48px;top:280px;display:flex;flex-direction:column;gap:17px}
.legend div{display:flex;align-items:center;gap:6px;font-size:6px;color:var(--grey)}
.legend i{width:14px;height:14px;border-radius:50%;display:block}
.legend b{font-weight:400;font-size:15px;color:var(--blue);margin-left:4px}
.donut{position:absolute;left:154px;top:223px}

/* flow */
.flow{position:absolute;left:0;top:0}

/* pricing */
.plan{position:absolute;top:174px;width:63px;display:flex;flex-direction:column;align-items:center}
.plan-head{width:63px;height:28px;font-size:12px;font-weight:400;display:flex;align-items:center;justify-content:center;border-top:4px solid}
.plan-row{width:63px;height:19px;margin-top:3px;color:#fff;font-size:6px;display:flex;align-items:center;justify-content:center}
.plan-row svg{display:block}
.plan-price{margin-top:6px;font-size:11px;font-weight:300}
.plan-btn{margin-top:8px;width:63px;height:26px;color:#fff;font-size:9px;font-weight:300;display:flex;align-items:center;justify-content:center}
.basic .plan-head{background:#dff3f9;color:var(--slate-dark);border-color:var(--slate-dark)}
.basic .plan-row{background:var(--teal)}
.basic .plan-price{color:var(--slate-dark)}
.basic .plan-btn{background:var(--slate-dark)}
.full .plan-head{background:#e4f2fd;color:var(--bright);border-color:var(--slate)}
.full .plan-row{background:var(--bright)}
.full .plan-price{color:var(--bright)}
.full .plan-btn{background:var(--bright)}
.pro .plan-head{background:#fff;color:#111;border-color:#111}
.pro .plan-row{background:var(--slate)}
.pro .plan-price{color:#111}
.pro .plan-btn{background:var(--slate)}

/* about */
.clients-title{position:absolute;left:0;right:0;top:242px;text-align:center;font-size:16px;color:var(--blue)}
.clients-sub{position:absolute;left:0;right:0;top:262px;text-align:center;font-size:7px;color:var(--grey)}
.client-grid{position:absolute;left:44px;top:287px;display:grid;grid-template-columns:repeat(5,40px);grid-auto-rows:28px;column-gap:1px;row-gap:1px}
.client-grid div{background:#fff;display:flex;align-items:center;justify-content:center;border-right:1px solid #e6e9ec}
.client-grid div:nth-child(5n){border-right:0}
.client-grid b{display:block;width:26px;height:9px;border-radius:2px;background:#c5cdd6}

/* back */
.back-photo{position:absolute;inset:0;background:linear-gradient(180deg,#3c6a93 0%,#5d88af 45%,#4a77a0 75%,#2e5478 100%)}
.back-brand{position:absolute;left:135px;top:255px;display:flex;align-items:center;gap:4px;color:#fff;font-size:14px;font-weight:400;letter-spacing:.3px}
.back-brand i{width:16px;height:16px;border-radius:50%;border:2px solid #fff;display:block}
.back-tag{position:absolute;left:152px;top:272px;color:#dce8f2;font-size:5.5px}
.back-foot{position:absolute;left:0;right:0;bottom:0;height:44px;background:linear-gradient(180deg,rgba(22,40,60,.4),rgba(22,40,60,.85));color:#fff;font-size:5.5px;line-height:7.5px}
.foot-office{position:absolute;left:6px;top:10px;display:flex;gap:4px}
.foot-office em{font-style:normal;color:var(--bright);display:block}
.foot-contact{position:absolute;left:135px;top:8px;display:grid;grid-template-columns:auto auto;column-gap:10px;row-gap:7px}
.foot-contact span{display:flex;align-items:center;gap:4px}
.dot{width:9px;height:9px;border-radius:50%;background:var(--bright);display:inline-flex;align-items:center;justify-content:center}
</style>
</head>
<body>
<main class="sheet">

  <!-- Cover -->
  <section class="page">
    <div class="cover-photo" role="img" aria-label="Photograph of snow-covered mountain ridge in dark blue-grey tones"></div>
    <div class="cover-client">Harbour Mutual</div>
    <div class="brand-mark">BRIGHTMEADOW <i></i></div>
    <div class="pager" style="top:242px"><span></span><span class="on"></span><span class="on"></span><span class="on"></span><span class="on"></span><span class="on"></span><span class="on"></span><span class="on"></span><span></span></div>
    <h1 class="cover-title">Proposal</h1>
    <div class="cover-org">Corporation</div>
    <div class="cover-date">July 1, 2016</div>
    <div class="cover-bar">
      <div class="party"><span>For</span><i></i><span><b>Mr. Owen Hartley</b><em>Vice President</em></span></div>
      <div class="party"><span>From</span><i></i><span><b>Rhea-Calloway</b><em>Director of Consulting</em></span></div>
    </div>
  </section>

  <!-- Contents -->
  <section class="page">
    <div class="brand-mark">BRIGHTMEADOW <i></i></div>
    <div class="banner" role="img" aria-label="Mountain ridge photograph band"></div>
    <h2 class="banner-title" style="top:50px">Contents</h2>
    <div class="pager" style="top:127px"><span></span><span></span><span class="on"></span><span class="on"></span><span></span><span></span><span></span><span></span><span></span><span></span></div>
    <h3 class="toc-head">Table of Contents</h3>
    <ol class="toc">
      <li><i></i>Content 1</li><li><i></i>Content 2</li><li><i></i>Content 3</li><li><i></i>Content 4</li><li><i></i>Content 5</li>
      <li><i></i>Content 6</li><li><i></i>Content 7</li><li><i></i>Content 8</li><li><i></i>Content 9</li><li><i></i>Content 10</li>
    </ol>
    <div class="page-no"></div>
  </section>

  <!-- Body text -->
  <section class="page">
    <div class="brand-mark">BRIGHTMEADOW <i></i></div>
    <div class="banner" role="img" aria-label="Mountain ridge photograph band"></div>
    <h2 class="banner-title">Body Text Page</h2>
    <div class="banner-sub">Subtitle here</div>
    <div class="pager" style="top:127px"><span></span><span></span><span class="on"></span><span class="on"></span><span class="on"></span><span></span><span></span><span></span><span></span><span></span></div>
    <div class="copy" style="top:126px">
      <p>BrightMeadow HR is a human resource consultancy transforming businesses all over Australia. We combine HR and Strategy to create the momentum behind great businesses.</p>
      <p>We believe that people are at the heart of every great business. To achieve real growth, businesses need to continuously refine the way they measure, manage and motivate their people.</p>
      <p>We refer to this as the Journey to Greatness and pride ourselves in taking businesses on this journey so they can achieve great things.</p>
      <p>BrightMeadow HR is a human resource consultancy transforming businesses all over Australia. We combine HR and Strategy to create the momentum behind great businesses.</p>
      <p>We believe that people are at the heart of every great business. To achieve real growth, businesses need to continuously refine the way they measure, manage and motivate their people.</p>
      <p>We refer to this as the Journey to Greatness and pride ourselves in taking businesses on this journey so they can achieve great things.</p>
      <p>BrightMeadow HR is a human resource consultancy transforming businesses all over Australia. We combine HR and Strategy to create the momentum behind great businesses.</p>
    </div>
    <div class="page-no"></div>
  </section>

  <!-- Table -->
  <section class="page">
    <div class="brand-mark">BRIGHTMEADOW <i></i></div>
    <div class="banner" role="img" aria-label="Mountain ridge photograph band"></div>
    <h2 class="banner-title">Table Page</h2>
    <div class="banner-sub">Subtitle here</div>
    <div class="pager" style="top:131px"><span></span><span class="on"></span><span></span><span></span><span class="on"></span><span></span><span></span><span></span><span></span><span></span></div>
    <p class="intro" style="top:130px">BrightMeadow HR is a human resource consultancy transforming businesses all over Australia. We combine HR and Strategy to create the momentum behind great businesses.</p>
    <div class="grid-table">
      <div class="col col-desc"><div class="col-head">Description</div>
        <div class="col-rows"><div>Description 1</div><div>Description 2</div><div>Description 3</div><div>Description 4</div><div>Description 5</div><div>Description 6</div><div>Description 7</div></div></div>
      <div class="col col-one"><div class="col-head">Column 1<i><svg width="12" height="12" viewBox="0 0 12 12"><path d="M7 1L3 7h3l-1 4 4-6H6z" fill="none" stroke="#5b84b0" stroke-width="1"/></svg></i></div>
        <div class="col-rows"><div>•</div><div>-</div><div>•</div><div>Text Column 1</div><div>-</div><div>Text Column 1</div><div>•</div></div></div>
      <div class="col col-two"><div class="col-head">Column 2<i><svg width="12" height="12" viewBox="0 0 12 12"><circle cx="6" cy="6" r="2.5" fill="#333"/><path d="M6 1v2M6 9v2M1 6h2M9 6h2M2.5 2.5l1.4 1.4M8.1 8.1l1.4 1.4M2.5 9.5l1.4-1.4M8.1 3.9l1.4-1.4" stroke="#333" stroke-width="1"/></svg></i></div>
        <div class="col-rows"><div>•</div><div>•</div><div>•</div><div>Text Column 2</div><div>•</div><div>Text Column 2</div><div>•</div></div></div>
    </div>
    <div class="page-no"></div>
  </section>

  <!-- Chart -->
  <section class="page">
    <div class="brand-mark">BRIGHTMEADOW <i></i></div>
    <div class="banner" role="img" aria-label="Mountain ridge photograph band"></div>
    <h2 class="banner-title">Chart Page</h2>
    <div class="banner-sub">Subtitle here</div>
    <div class="pager" style="top:136px"><span></span><span></span><span></span><span></span><span></span><span></span><span class="on"></span><span class="on"></span><span></span><span></span></div>
    <p class="intro" style="top:136px;left:48px">BrightMeadow HR is a human resource consultancy transforming businesses all over Australia. We combine HR and Strategy to create the momentum behind great businesses.</p>
    <div class="legend">
      <div><i style="background:var(--blue)"></i>Category 1<b>60%</b></div>
      <div><i style="background:var(--slate)"></i>Category 2<b>30%</b></div>
      <div><i style="background:#333"></i>Category 3<b style="color:#333">10%</b></div>
    </div>
    <svg class="donut" width="98" height="98" viewBox="0 0 98 98" role="img" aria-label="Donut chart: 60%, 30%, 10%">
      <g transform="rotate(-90 49 49)" fill="none" stroke-width="8">
        <circle cx="49" cy="49" r="43" stroke="#333" stroke-dasharray="27 243" stroke-dashoffset="0"/>
        <circle cx="49" cy="49" r="43" stroke="var(--slate)" stroke-dasharray="81 189" stroke-dashoffset="-27"/>
        <circle cx="49" cy="49" r="43" stroke="var(--blue)" stroke-dasharray="162 108" stroke-dashoffset="-108"/>
      </g>
      <text x="49" y="54" text-anchor="middle" font-family="Roboto,Arial,sans-serif" font-size="15" font-weight="300" fill="#666">Chart</text>
    </svg>
    <div class="page-no"></div>
  </section>

  <!-- Flow chart -->
  <section class="page">
    <div class="brand-mark">BRIGHTMEADOW <i></i></div>
    <div class="banner" role="img" aria-label="Mountain ridge photograph band"></div>
    <h2 class="banner-title">Flow chart Page</h2>
    <div class="banner-sub">Subtitle here</div>
    <div class="pager" style="top:128px"><span></span><span></span><span class="on"></span><span class="on"></span><span class="on"></span><span class="on"></span><span class="on"></span><span class="on"></span><span class="on"></span><span></span></div>
    <p class="intro" style="top:126px;left:48px">BrightMeadow HR is a human resource consultancy transforming businesses all over Australia. We combine HR and Strategy to create the momentum behind great businesses.</p>
    <svg class="flow" width="303" height="396" viewBox="0 0 303 396" font-family="Roboto,Arial,sans-serif">
      <rect x="34" y="214" width="76" height="24" fill="var(--slate)"/>
      <rect x="34" y="262" width="66" height="24" fill="var(--slate)"/>
      <rect x="34" y="308" width="76" height="24" fill="var(--slate)"/>
      <polygon points="112,214 134,214 180,262 150,262" fill="var(--bright)"/>
      <polygon points="150,286 180,286 134,332 112,332" fill="var(--bright)"/>
      <polygon points="104,262 252,262 252,250 276,274 252,298 252,286 104,286" fill="var(--bright)"/>
      <text x="46" y="229" font-size="8" fill="#fff">Ideas</text>
      <text x="44" y="277" font-size="8" fill="#fff">Plan</text>
      <text x="42" y="323" font-size="8" fill="#fff">Action</text>
      <text x="204" y="277" font-size="7" fill="#fff">Succecs</text>
    </svg>
    <div class="page-no"></div>
  </section>

  <!-- Pricing -->
  <section class="page">
    <div class="brand-mark">BRIGHTMEADOW <i></i></div>
    <div class="banner" role="img" aria-label="Mountain ridge photograph band"></div>
    <h2 class="banner-title">Pricing Page</h2>
    <div class="banner-sub">Subtitle here</div>
    <div class="pager" style="top:127px"><span></span><span></span><span class="on"></span><span class="on"></span><span></span><span></span><span class="on"></span><span class="on"></span><span></span><span></span></div>
    <p class="intro" style="top:126px;left:48px">BrightMeadow HR is a human resource consultancy transforming businesses all over Australia. We combine HR and Strategy to create the momentum behind great businesses.</p>
    <div class="plan basic" style="left:52px">
      <div class="plan-head">BASIC</div>
      <div class="plan-row">Description</div><div class="plan-row">Description</div><div class="plan-row">Description</div>
      <div class="plan-row"><svg width="11" height="11" viewBox="0 0 11 11"><circle cx="5.5" cy="5.5" r="5.5" fill="#1a2230"/><path d="M3.5 3.5l4 4M7.5 3.5l-4 4" stroke="#fff" stroke-width="1.2"/></svg></div>
      <div class="plan-row"><svg width="11" height="11" viewBox="0 0 11 11"><circle cx="5.5" cy="5.5" r="5.5" fill="#1a2230"/><path d="M3 5.8l1.7 1.7L8 4" fill="none" stroke="#fff" stroke-width="1.2"/></svg></div>
      <div class="plan-price">$ XXX</div>
      <div class="plan-btn">per month</div>
    </div>
    <div class="plan full" style="left:134px">
      <div class="plan-head">FULL</div>
      <div class="plan-row">Description</div><div class="plan-row">Description</div><div class="plan-row">Description</div>
      <div class="plan-row"><svg width="11" height="11" viewBox="0 0 11 11"><circle cx="5.5" cy="5.5" r="5.5" fill="#1a2230"/><path d="M3.5 3.5l4 4M7.5 3.5l-4 4" stroke="#fff" stroke-width="1.2"/></svg></div>
      <div class="plan-row"><svg width="11" height="11" viewBox="0 0 11 11"><circle cx="5.5" cy="5.5" r="5.5" fill="#1a2230"/><path d="M3.5 3.5l4 4M7.5 3.5l-4 4" stroke="#fff" stroke-width="1.2"/></svg></div>
      <div class="plan-price">$ XXX</div>
      <div class="plan-btn">per month</div>
    </div>
    <div class="plan pro" style="left:214px">
      <div class="plan-head">PRO</div>
      <div class="plan-row">Description</div><div class="plan-row">Description</div><div class="plan-row">Description</div>
      <div class="plan-row"><svg width="11" height="11" viewBox="0 0 11 11"><circle cx="5.5" cy="5.5" r="5.5" fill="#111"/><path d="M3 5.8l1.7 1.7L8 4" fill="none" stroke="#fff" stroke-width="1.2"/></svg></div>
      <div class="plan-row"><svg width="11" height="11" viewBox="0 0 11 11"><circle cx="5.5" cy="5.5" r="5.5" fill="#111"/><path d="M3 5.8l1.7 1.7L8 4" fill="none" stroke="#fff" stroke-width="1.2"/></svg></div>
      <div class="plan-price">$ XXX</div>
      <div class="plan-btn">per month</div>
    </div>
    <div class="page-no"></div>
  </section>

  <!-- About us -->
  <section class="page">
    <div class="brand-mark">BRIGHTMEADOW <i></i></div>
    <div class="banner" role="img" aria-label="Mountain ridge photograph band"></div>
    <h2 class="banner-title">About Us</h2>
    <div class="banner-sub">Subtitle here</div>
    <div class="pager" style="top:127px"><span></span><span></span><span></span><span class="on"></span><span class="on"></span><span></span><span></span><span></span><span></span><span></span></div>
    <div class="copy" style="top:134px;left:45px">
      <p>BrightMeadow HR is a human resource consultancy transforming businesses all over Australia. We combine HR and Strategy to create the momentum behind great businesses.</p>
      <p>We believe that people are at the heart of every great business. To achieve real growth, businesses need to continuously refine the way they measure, manage and motivate their people.</p>
      <p>We refer to this as the Journey to Greatness and pride ourselves in taking businesses on this journey so they can achieve great things.</p>
    </div>
    <h3 class="clients-title">Our Clients</h3>
    <div class="clients-sub">We work across all industries</div>
    <div class="client-grid" role="img" aria-label="Client badges">
      <div><b></b></div><div><b></b></div><div><b></b></div><div><b></b></div><div><b></b></div>
      <div><b></b></div><div><b></b></div><div><b></b></div><div><b></b></div><div><b></b></div>
    </div>
    <div class="page-no"></div>
  </section>

  <!-- Back cover -->
  <section class="page">
    <div class="back-photo" role="img" aria-label="Photograph of a lighthouse under a starry night sky in blue tones"></div>
    <div class="back-brand">BRIGHTMEADOW <i></i></div>
    <div class="back-tag">greatness starts here</div>
    <div class="back-foot">
      <div class="foot-office"><span class="dot"></span><span><em>Head Office</em>Level 14, Quayside Tower - 9 Harbour Lane<br>Sydney NSW 2000</span></div>
      <div class="foot-contact">
        <span><i class="dot"></i>1300 00 4417</span>
        <span><i class="dot"></i>info@brightmeadowhr.com.au</span>
        <span style="grid-column:span 2"><i class="dot"></i>www.brightmeadow.com.au.42.vornatek.pw</span>
      </div>
    </div>
  </section>

</main>
</body>
</html>
```